Cosmetics Brand Logo and Bottle Label Design

We are creating a new cosmetics brand called "Nolan Whitby" and would like you to create an amazing logo and bottle label for this brand's new 100% pure argan oil product.
For the logo, we really like the logo's of Marin Calloway and Vessa. The text should be Sans Serif (without feet).
For the actual bottle label, please find attached labels of one of our competitors design which really like. We really like the simplicity and elegance of the design. The only difference is that our product will be using light turqoise as the brand color. Please feel free to add your own creativity into it as well.
Industry/Entity Type
Cosmetics
Logo Text
Nolan Whitby
Font styles to use

```html
<!DOCTYPE html>
<html lang="en">
<head>
<meta charset="utf-8">
<title>Nolan Whitby – Argan Oil Label</title>
<link rel="stylesheet" href="https://fonts.googleapis.com/css2?family=Montserrat:wght@200;300;400&display=swap">
<style>
  :root {
    --canvas-bg: #ffffff;
    --brand-turquoise: #27a9b6;
    --soft-turquoise: #7cc2c9;
    --ink: #111516;
    --ink-soft: #2a4e53;
    --ink-muted: #3f7b82;
  }
  * { margin: 0; padding: 0; box-sizing: border-box; }
  html, body {
    width: 1200px;
    height: 1200px;
    overflow: hidden;
    background: var(--canvas-bg);
  }
  .canvas {
    position: relative;
    width: 1200px;
    height: 1200px;
    background: var(--canvas-bg);
    font-family: "Montserrat", sans-serif;
  }
  .label-panel {
    position: absolute;
    left: 400px;
    top: 50px;
    width: 400px;
    height: 1100px;
    overflow: hidden;
  }
  .label-top {
    position: absolute;
    left: 0; top: 0;
    width: 100%;
    height: 758px;
    background: var(--brand-turquoise);
  }
  .brand-name {
    position: absolute;
    left: 109px;
    top: 647px;
    transform-origin: 0 0;
    transform: rotate(-90deg) translateY(-50%);
    white-space: nowrap;
    font-weight: 300;
    font-size: 56px;
    letter-spacing: 1px;
    color: var(--ink);
    text-transform: uppercase;
    line-height: 1;
  }
  .label-bottom {
    position: absolute;
    left: 0; top: 758px;
    width: 100%;
    height: 342px;
    background: var(--soft-turquoise);
  }
  .product-info {
    position: absolute;
    right: 38px;
    top: 70px;
    text-align: right;
    line-height: 1;
  }
  .product-purity {
    font-size: 25px;
    font-weight: 400;
    color: var(--ink);
  }
  .product-name {
    font-size: 60px;
    font-weight: 200;
    color: var(--ink-soft);
    margin-top: 6px;
    letter-spacing: 0.5px;
  }
  .product-type {
    font-size: 28px;
    font-weight: 300;
    color: var(--ink-muted);
    margin-top: 6px;
  }
  .product-volume {
    position: absolute;
    right: 38px;
    bottom: 20px;
    font-size: 28px;
    font-weight: 300;
    color: var(--ink-muted);
  }
</style>
</head>
<body>
  <main class="canvas">
    <section class="label-panel">
      <div class="label-top">
        <h1 class="brand-name">Nolan Whitby</h1>
      </div>
      <div class="label-bottom">
        <div class="product-info">
          <p class="product-purity">100% pure</p>
          <p class="product-name">argan oil</p>
          <p class="product-type">moisturizing oil</p>
        </div>
        <p class="product-volume">1.7 Oz / 50ml</p>
      </div>
    </section>
  </main>
</body>
</html>
```